Lobby Sentinel Staffing

Lobby sentinel is similar to a security company but is more concierge/customer service oriented. Picture a security guard in a suit working at a condo or office building. Our thoughts for a logo is a silhouette of a male/female sitting at a desk or some type of crest but were open to creative ideas.

Target Market(s)

Property Managers

Industry/Entity Type

Security

Font styles to use
Serif

Requirements
Must have
• Male/Female sitting professionally at a desk.
Nice to have
• Vertical card
Should not have
• Cartoons

```html
<!DOCTYPE html>
<html lang="en">
<head>
<meta charset="utf-8">
<title>Lobby Sentinel Staffing – Business Card</title>
<link href="https://fonts.googleapis.com/css2?family=Cinzel:wght@400;700&display=swap" rel="stylesheet">
<style>
  :root{
    --page:#ecebe8;
    --card:#ffffff;
    --sky:#2ba3d9;
    --sky-soft:#bfe3f4;
    --violet:#36338c;
    --violet-soft:#6f6bb8;
    --cyan-text:#2aa6d6;
    --ink:#5a5a66;
  }
  *{box-sizing:border-box;margin:0;padding:0}
  html,body{width:1200px;height:600px;overflow:hidden}
  body{background:var(--page);font-family:"Cinzel",serif;position:relative}

  .card{position:absolute;top:157px;width:500px;height:286px;background:var(--card);
        box-shadow:0 6px 18px rgba(0,0,0,.18);overflow:hidden}
  .card--front{left:60px}
  .card--back{left:640px}

  /* front */
  .front-art{position:absolute;inset:0;
        background:linear-gradient(35deg,var(--sky) 0%,var(--sky-soft) 35%,rgba(255,255,255,0) 62%)}
  .front-art__people{position:absolute;left:140px;top:46px;width:190px;height:170px;
        background:linear-gradient(180deg,rgba(111,107,184,.3),rgba(80,70,160,.8));
        border-radius:90px 90px 0 0}
  .company-name{position:absolute;left:22px;bottom:26px;font-weight:700;font-size:25px;
        color:var(--violet);letter-spacing:.5px;font-variant:small-caps;line-height:1}

  .contact{position:absolute;right:24px;top:30px;text-align:right;color:var(--ink)}
  .contact__name{font-size:17px;color:var(--cyan-text);font-weight:700;font-variant:small-caps}
  .contact__role{font-size:9px;letter-spacing:1px;margin-top:3px}
  .contact__address{font-size:9px;letter-spacing:.5px;margin-top:16px;line-height:1.5}
  .contact__list{list-style:none;margin-top:18px;font-size:9px;letter-spacing:.5px}
  .contact__list li{display:flex;justify-content:flex-end;align-items:center;gap:7px;height:15px}
  .contact__list svg{width:11px;height:11px}

  /* back */
  .back-art{position:absolute;inset:0;
        background:linear-gradient(135deg,var(--sky) 0%,#3b7fd0 55%,var(--violet) 100%)}
  .back-art__people{position:absolute;left:90px;top:70px;width:320px;height:216px;
        background:linear-gradient(180deg,rgba(80,70,160,.5),rgba(54,51,140,.95));
        border-radius:140px 140px 0 0}
</style>
</head>
<body>
  <section class="card card--front">
    <div class="front-art">
      <div class="front-art__people" role="img" aria-label="Silhouettes of professional staff in suits at a front desk"></div>
    </div>
    <h1 class="company-name">Lobby Sentinel Staffing</h1>

    <div class="contact">
      <p class="contact__name">Marcus Hale</p>
      <p class="contact__role">MANAGER</p>
      <p class="contact__address">218 HARBOR LANE,<br>WESTBROOK</p>
      <ul class="contact__list">
        <li>4120 337 905
          <svg viewBox="0 0 12 12"><rect width="12" height="12" rx="2" fill="#2aa6d6"/><path d="M3.5 2.5h2v2l-1 .8a5 5 0 0 0 2.2 2.2l.8-1h2v2a1 1 0 0 1-1 1A6.5 6.5 0 0 1 2.5 3.5a1 1 0 0 1 1-1z" fill="#fff"/></svg></li>
        <li>318 462 907 1
          <svg viewBox="0 0 12 12"><rect width="12" height="12" rx="2" fill="#2aa6d6"/><rect x="4" y="2" width="4" height="8" rx="1" fill="#fff"/></svg></li>
        <li>INFO@LSS.COM
          <svg viewBox="0 0 12 12"><rect width="12" height="12" rx="2" fill="#2aa6d6"/><rect x="2.5" y="3.5" width="7" height="5" fill="#fff"/><path d="M2.5 3.5 6 6.5l3.5-3" stroke="#2aa6d6" fill="none" stroke-width=".8"/></svg></li>
        <li>WWW.LSS.COM
          <svg viewBox="0 0 12 12"><rect width="12" height="12" rx="2" fill="#2aa6d6"/><circle cx="6" cy="6" r="3.5" fill="none" stroke="#fff" stroke-width="1"/><path d="M2.5 6h7M6 2.5v7" stroke="#fff" stroke-width=".8"/></svg></li>
      </ul>
    </div>
  </section>

  <section class="card card--back">
    <div class="back-art">
      <div class="back-art__people" role="img" aria-label="Silhouettes of suited lobby staff working together"></div>
    </div>
  </section>
</body>
</html>
```